Business Cards for Harbourline Coatings Pty Ltd

Hi every one i need a design for my buisness cards. I Want my logo in it and the name of the company needs to stand out Harbourline Coatings Pty Ltd. I want the background of the buisness cards black and i want the font to stand out in either a white or a silver stylish text. I want the design to be simple but original not to in your face if you know what i mean. I want on the back of the buisness cards to have the services that my buisness offers.
• Interior/Exterior
• Residential/Commercial
• Special effects/Texture Coatings
• Water Damage Repair
• Fully qualified
• Pensioner Discount
• 10 Year guarantee
• Fully Insured
• Obligation free quotes
full internal repaints include a proffesionla cleaning service
I want the services on the back to be layed out in an originall way not just dot points. If possible could my logo take up the whole back ground of the back but the text with the services be kind of like transparent so u cvan still see the logo i dont know if its possible it woiuld just look cool if possible. When i pick a design ill give my contact details to the designer to add to the design at the end. Any questions please just ask! Ill upload my logo.
Conatcs will include office phone: Mobile: E-mail - dale@harbourlinecoatings.com.au, Ill also have a Postal address which is a PO Box and my website is www.harbourlinecoatings.com.au

```html
<!DOCTYPE html>
<html lang="en">
<head>
<meta charset="utf-8">
<title>Harbourline Coatings Pty Ltd – Business Cards</title>
<link href="https://fonts.googleapis.com/css2?family=Arimo:wght@400;700&display=swap" rel="stylesheet">
<style>
  :root {
    --page: #e6e6e3;
    --card-black: #000000;
    --lime: #9ccc3c;
    --ink: #1a1a1a;
    --white: #ffffff;
    --silver: #e4e4e4;
  }
  * { box-sizing: border-box; margin: 0; padding: 0; }
  html, body {
    width: 1200px; height: 900px; overflow: hidden;
    background: var(--page);
    font-family: "Arimo", Arial, sans-serif;
  }
  .stage { position: relative; width: 1200px; height: 900px; }
  .card {
    position: absolute; top: 282px;
    width: 496px; height: 302px;
    border-radius: 18px; overflow: hidden;
    background: var(--card-black);
    box-shadow: 0 6px 18px rgba(0,0,0,.25);
  }
  .card--front { left: 100px; }
  .card--back { left: 629px; }
  .card__band {
    position: absolute; left: 0; right: 0; bottom: 0; height: 122px;
    background: var(--lime);
  }
  /* brand */
  .brand { position: absolute; text-align: center; }
  .brand__mark {
    display: block; margin: 0 auto;
    background: var(--lime); border-radius: 3px;
  }
  .brand__name {
    color: var(--silver); font-weight: 700; line-height: 1.15;
    white-space: nowrap;
  }
  .brand__suffix {
    color: var(--lime); font-weight: 700; font-size: 13px; line-height: 1.2;
  }
  .card--front .brand { left: 250px; width: 236px; top: 20px; }
  .card--front .brand__mark { width: 82px; height: 82px; margin-bottom: 10px; }
  .card--front .brand__name { font-size: 15.5px; }
  .card--back .brand { left: 0; right: 0; top: 37px; }
  .card--back .brand__mark { width: 72px; height: 72px; margin-bottom: 10px; }
  .card--back .brand__name { font-size: 18px; }
  /* contacts */
  .contacts { position: absolute; left: 40px; top: 48px; list-style: none; }
  .contacts li {
    display: flex; align-items: center; gap: 9px;
    color: var(--white); font-size: 12px; height: 22px;
  }
  .contacts svg { width: 11px; height: 11px; fill: none; stroke: var(--lime); stroke-width: 1.6; flex: none; }
  /* address */
  .address { position: absolute; left: 43px; top: 202px; color: var(--ink); font-size: 12.5px; line-height: 23px; }
  .address__company { font-weight: 700; }
  .person { position: absolute; left: 276px; width: 180px; top: 212px; text-align: center; }
  .person__name { color: var(--ink); font-weight: 700; font-size: 21px; line-height: 1.1; }
  .person__role { color: var(--white); font-size: 15px; line-height: 1.1; }
  /* services */
  .services {
    position: absolute; left: 0; right: 0; bottom: 0; height: 122px;
    display: flex; flex-direction: column; justify-content: center; gap: 7px;
    color: var(--ink); font-size: 11px; text-align: center;
  }
</style>
</head>
<body>
<main class="stage">
  <section class="card card--front" aria-label="Business card front">
    <div class="card__band"></div>
    <ul class="contacts">
      <li><svg viewBox="0 0 12 12"><path d="M2 1h3v3L3.5 5.5a7 7 0 0 0 3 3L8 7h3v3c0 1-1 1-1 1A9 9 0 0 1 1 2s0-1 1-1z"/></svg>(02) 5550 1827</li>
      <li><svg viewBox="0 0 12 12"><rect x="3" y="1" width="6" height="10" rx="1"/><path d="M5 9h2"/></svg>0400 555 318</li>
      <li><svg viewBox="0 0 12 12"><rect x="1" y="2.5" width="10" height="7"/><path d="M1 2.5l5 4 5-4"/></svg>dale@harbourlinecoatings.com.au</li>
      <li><svg viewBox="0 0 12 12"><circle cx="6" cy="6" r="5"/><path d="M1 6h10M6 1c-2.5 3-2.5 7 0 10M6 1c2.5 3 2.5 7 0 10"/></svg>www.harbourlinecoatings.com.au</li>
    </ul>
    <div class="brand">
      <span class="brand__mark"></span>
      <p class="brand__name">HARBOURLINE COATINGS</p>
      <p class="brand__suffix">PTY LTD</p>
    </div>
    <div class="address">
      <p class="address__company">Harbourline Coatings Pty Ltd.</p>
      <p>Kestrel St. No 18 Marlow NSW</p>
      <p>PO BOX 40871</p>
    </div>
    <div class="person">
      <p class="person__name">Dale Whitmore</p>
      <p class="person__role">founder</p>
    </div>
  </section>

  <section class="card card--back" aria-label="Business card back">
    <div class="card__band"></div>
    <div class="brand">
      <span class="brand__mark"></span>
      <p class="brand__name">HARBOURLINE COATINGS</p>
      <p class="brand__suffix">PTY LTD</p>
    </div>
    <div class="services">
      <p>Interior/Exterior • Residential/Commercial • Special effects/Texture Coatings</p>
      <p>Water Damage Repair • Fully qualified • Pensioner Discount • 10 Year guarantee</p>
      <p>Fully Insured • Obligation free quotes</p>
    </div>
  </section>
</main>
</body>
</html>
```